Hello,
We’re looking for a new WordPress website for Gather Your Light, our company offering unique well-being retreats and workshops.
We currently have a website online (you can consult it : www.gatheryourlight.ch), but we now need to build a new site on WordPress — more flexible, more intuitive to manage, and better aligned with our evolving needs.

What we’re looking for:
A new userfriendly WordPress site, with:
Inspiring, elegant, and modern design
Smooth user experience on desktop and mobile
Innovative design proposals – we want to be inspired !
SEO best practices
Respect of our existing color palette
The final website will need to be set up on our existing hosting provider (details can be shared later)

Pages to Include:
- Home
- Our Story
- Our Stays - with links to 5 individual pages, each describing one of our stays in detail.
- Activities – with potential links to individual descriptive pages
- Agenda
- Our Charter
- The Team
- Contact
- Blog

Required Features:
- Space for photos and videos
- Sections for testimonials and press articles
- Blog/article layout with strong readability
- Easy-to-update backend for future content
- Newsletter sign-up (pop-up and in footer)
- Additional pop-up on/off
- “Request info” buttons
- “Booking request” buttons
- Integration of our 4 pillars - Breathe · Feel · Connect · Experience - in the design (They’re currently in the footer, but we’re open to creative suggestions)

Who we are :
Gather Your Light offers well-being and personal growth stays but with a very different spirit.
We’re not a classic wellness brand. Our approach is professional, joyful, and grounded.
We create spaces where people can take a real break — breathe, slow down, and reconnect with themselves.
During our stays, people are welcomed like friends:
with warmth, respect, and no pressure.
Each program combines practices like breathwork, movement, creativity, coaching, and massages in a relaxed, beautiful setting of the French Alps.
What makes us different:
A friendly and down-to-earth atmosphere
A wide mix of activities.
A mix of inner work and simple pleasures
Private rooms, nourishing food, and shared moments
Time to talk, to laugh, to walk, or just be silent together - and feel free to be yourself
Our guests come to pause.
They leave feeling lighter, aligned, and full of life

```html
<!DOCTYPE html>
<html lang="en">
<head>
<meta charset="UTF-8">
<title>Gather Your Light — Well-being Retreats</title>
<link href="https://fonts.googleapis.com/css2?family=Poppins:wght@300;400;500;600;700&display=swap" rel="stylesheet">
<style>
:root{
  --blue:#1a3d9c;
  --navy:#0f1b34;
  --teal:#5aaebc;
  --ink:#2b2f38;
  --muted:#6b7080;
  --ice:#dcedf1;
  --paper:#f4f5f8;
  --white:#ffffff;
}
*{margin:0;padding:0;box-sizing:border-box}
html,body{width:1200px;height:4074px;overflow:hidden}
body{font-family:"Poppins",sans-serif;color:var(--ink);background:var(--white);position:relative}
section,header,footer,.topbar{position:absolute;left:0;width:1200px}
.abs{position:absolute}
.btn{position:absolute;display:flex;align-items:center;justify-content:center;background:var(--teal);color:var(--white);font-size:14px;font-weight:500;border-radius:5px}

.topbar{top:0;height:38px;background:var(--blue);color:var(--white);font-size:12px}
.dot{width:14px;height:14px;border-radius:50%;background:var(--white);opacity:.85}

.nav{top:38px;height:88px;background:var(--paper)}
.brand{left:161px;top:18px;color:var(--blue);font-size:34px;font-weight:600;letter-spacing:1px;line-height:1}
.brand small{display:block;font-size:10px;font-weight:600;letter-spacing:9px;color:var(--teal);margin-top:3px}
.menu{left:356px;top:36px;display:flex;gap:27px;font-size:13px;color:#2d3448;letter-spacing:.3px}

.hero{top:126px;height:560px;background:
  linear-gradient(180deg,rgba(255,255,255,0) 0%,rgba(255,255,255,0) 100%),
  radial-gradient(ellipse 60% 20% at 50% 22%,rgba(235,238,242,.8),rgba(235,238,242,0)),
  linear-gradient(180deg,#b7c3cf 0%,#8b9aa6 18%,#5f6f55 34%,#4d6a36 52%,#5d8a34 72%,#6a9a3a 100%)}
.hero-title{left:0;width:1200px;text-align:center;color:var(--white);font-weight:600}
.hero-title.one{top:172px;font-size:92px;line-height:1}
.hero-title.two{top:275px;font-size:74px;line-height:1;letter-spacing:1px}
.hero-sub{top:360px;left:0;width:1200px;text-align:center;color:var(--white);font-size:15px;line-height:1.25}

.pillars{top:686px;left:147px;width:906px;height:89px;background:var(--white);border-radius:0 0 14px 14px;position:absolute}
.pillar{position:absolute;top:-50px;width:120px;height:120px;border-radius:50%;background:var(--white);box-shadow:0 4px 14px rgba(0,0,0,.12);display:flex;flex-direction:column;align-items:center;justify-content:center}
.pillar .art{width:62px;height:52px;border-radius:26px}
.pillar span{font-family:Georgia,serif;font-size:10px;color:#6d6d6d;margin-top:6px;letter-spacing:.5px}

.history{top:686px;height:554px;background:var(--blue);z-index:-1}
.history-photo{left:161px;top:253px;width:440px;height:301px;background:
  linear-gradient(180deg,rgba(0,0,0,0) 55%,rgba(60,52,30,.7)),
  linear-gradient(160deg,#a5afbb,#6c7683 45%,#4e5a4a);border-radius:4px 4px 0 0}
.eyebrow{font-size:13px}
.history .eyebrow{left:674px;top:196px;color:var(--white)}
.history h2{left:674px;top:222px;color:var(--white);font-size:32px;font-weight:600}
.history p{left:675px;width:360px;color:var(--white);font-size:13.5px;line-height:1.45}

.head{left:0;width:1200px;text-align:center}
.head .eyebrow{color:var(--blue)}
.head h2{font-size:31px;font-weight:600;margin-top:8px;line-height:1.2}
.head p{font-size:13px;color:var(--muted);margin:8px auto 0;width:540px;line-height:1.25}

.stays{top:1240px;height:555px;background:var(--white)}
.stay{top:205px;width:277px;height:210px;border-radius:6px;overflow:hidden}
.stay .label{position:absolute;left:13px;bottom:18px;color:var(--white);font-size:17px;font-weight:600}
.stay .go{position:absolute;right:12px;bottom:13px;width:30px;height:30px;border-radius:50%;background:var(--white);display:flex;align-items:center;justify-content:center}

.gallery{top:1795px;height:766px;background:linear-gradient(180deg,#2a3547,#1e2533 60%,#262a2e)}
.gallery .head .eyebrow,.gallery .head h2,.gallery .head p{color:var(--white)}
.tile{border-radius:4px}
.play{position:absolute;left:50%;top:50%;transform:translate(-30%,-50%)}

.testi{top:2561px;height:527px;background:var(--ice)}
.card{top:220px;width:384px;height:180px;background:var(--white);border-radius:3px;padding:32px}
.avatar{width:58px;height:58px;background:linear-gradient(160deg,#c5b7a6,#6c6a74);border-radius:3px}
.who{position:absolute;left:103px;top:44px;font-size:14px;line-height:1.45}
.who b{font-weight:600}
.quote{position:absolute;right:28px;top:30px;font-family:Georgia,serif;font-size:70px;color:var(--teal);line-height:1;opacity:.8}
.card p{position:absolute;left:32px;top:114px;font-size:13px;color:var(--muted);line-height:1.5;white-space:nowrap}

.blog{top:3088px;height:672px;background:var(--white)}
.post{top:204px;width:418px;height:322px;background:var(--paper);border-radius:4px;overflow:hidden}
.post .body{position:absolute;left:23px;top:34px;width:240px}
.cat{font-size:11px;color:var(--teal);letter-spacing:1px}
.date{font-size:11px;color:var(--muted);margin-top:4px}
.post h3{font-size:17px;font-weight:600;line-height:1.4;margin-top:30px;white-space:nowrap}
.post p{font-size:12px;color:var(--muted);line-height:1.6;margin-top:10px;white-space:nowrap}
.more{display:inline-block;margin-top:26px;font-size:11px;color:var(--blue);border-bottom:1px solid var(--blue);padding-bottom:3px}
.post .pic{position:absolute;right:0;top:0;width:143px;height:322px}

.foot{top:3760px;height:314px;background:var(--navy);color:var(--white)}
.foot .brand{left:160px;top:50px;color:var(--white);font-size:40px;line-height:1}
.foot .brand small{color:var(--teal);font-size:11px;letter-spacing:14px;margin-top:4px}
.foot-about{left:161px;top:124px;width:290px;font-size:12px;line-height:1.5}
.foot h4{font-size:16px;font-weight:500}
.links{list-style:none;font-size:12px;line-height:27px;margin-top:10px}
.contact-row{display:flex;align-items:center;gap:12px;font-size:12.5px;margin-bottom:14px}
.ico{width:26px;height:26px;border-radius:50%;background:var(--teal);display:flex;align-items:center;justify-content:center}
.rule{left:161px;top:257px;width:878px;height:1px;background:rgba(255,255,255,.25)}
.copy{left:0;top:278px;width:1200px;text-align:center;font-size:12.5px}
</style>
</head>
<body>

<div class="topbar">
  <div class="abs dot" style="left:159px;top:12px"></div>
  <div class="abs dot" style="left:195px;top:12px"></div>
  <div class="abs dot" style="left:235px;top:12px"></div>
  <svg class="abs" style="left:712px;top:12px" width="14" height="14" viewBox="0 0 24 24"><path fill="#fff" d="M6.6 10.8a15 15 0 0 0 6.6 6.6l2.2-2.2c.3-.3.7-.4 1-.2 1.1.4 2.3.6 3.6.6.6 0 1 .4 1 1V20c0 .6-.4 1-1 1A17 17 0 0 1 3 4c0-.6.4-1 1-1h3.5c.6 0 1 .4 1 1 0 1.2.2 2.4.6 3.6.1.3 0 .7-.2 1z"/></svg>
  <div class="abs" style="left:734px;top:11px">+41 22 555 01 47</div>
  <svg class="abs" style="left:855px;top:13px" width="15" height="12" viewBox="0 0 24 18"><rect x="1" y="1" width="22" height="16" rx="2" fill="none" stroke="#fff" stroke-width="2"/><path d="M2 2l10 8 10-8" fill="none" stroke="#fff" stroke-width="2"/></svg>
  <div class="abs" style="left:886px;top:10px">info@gatheryourlight.ch</div>
</div>

<header class="nav">
  <div class="abs brand">GATHER<small>YOUR LIGHT</small></div>
  <nav class="abs menu">
    <span>WELCOME</span><span>OUR HISTORY</span><span>OUR STAYS</span><span>THE AGENDA</span><span>OUR CHARTER</span><span>THE TEAM</span><span>CONTACT</span>
  </nav>
</header>

<section class="hero" role="img" aria-label="Alpine meadow with a chalet beneath snowy mountains and low clouds">
  <h1 class="abs hero-title one">Gather</h1>
  <div class="abs hero-title two">YOUR LIGHT</div>
  <p class="abs hero-sub">If you are in need of a real pause, warm, grounded and friendly<br>well-being stays, look no further than our retreats.</p>
  <div class="btn" style="left:520px;top:419px;width:161px;height:40px">Booking Request</div>
</section>

<div class="pillars">
  <div class="pillar" style="left:90px"><div class="art" role="img" aria-label="Breathe pillar illustration" style="background:radial-gradient(#efe6da,#d9cbb8)"></div><span>BREATHE</span></div>
  <div class="pillar" style="left:291px"><div class="art" role="img" aria-label="Feel pillar illustration" style="background:radial-gradient(#f6c3c3,#e0474f)"></div><span>FEEL</span></div>
  <div class="pillar" style="left:493px"><div class="art" role="img" aria-label="Connect pillar illustration" style="background:radial-gradient(#f39ab8,#d8324d)"></div><span>CONNECT</span></div>
  <div class="pillar" style="left:697px"><div class="art" role="img" aria-label="Experience pillar illustration" style="background:radial-gradient(#cfe6c0,#3f8a3a)"></div><span>EXPERIENCE</span></div>
</div>

<section class="history">
  <div class="abs history-photo" role="img" aria-label="Hiking couple with backpacks in front of a mountain valley"></div>
  <div class="abs eyebrow">History</div>
  <h2 class="abs">Our History</h2>
  <p class="abs" style="top:270px">GATHER Your Light is, above all, a story of men and women, a story of encounters and desire, a desire to share, a desire to refocus and a desire to breathe.</p>
  <p class="abs" style="top:348px">Absorbed in a world that is running out of time, it has become essential to find a little personal space to take precisely the time we are so desperately running after.</p>
  <div class="btn" style="left:675px;top:455px;width:161px;height:40px">Learn More</div>
</section>

<section class="stays">
  <div class="abs head" style="top:56px">
    <div class="eyebrow">Our Stays</div>
    <h2>Our Stays</h2>
    <p>Welcome to our Gather Your Light chapters dedicated to empowering guests with valuable knowledge and resources.</p>
  </div>
  <div class="abs stay" style="left:161px;background:linear-gradient(180deg,rgba(0,0,0,0) 60%,rgba(0,0,0,.35)),linear-gradient(160deg,#7aa6d0,#3b5a7a 55%,#6a5532)" role="img" aria-label="Guest on a wooden terrace looking over a misty valley">
    <span class="label">Instant</span><span class="go"><svg width="12" height="12" viewBox="0 0 12 12"><path d="M2 10L10 2M4 2h6v6" fill="none" stroke="#5aaebc" stroke-width="1.6"/></svg></span>
  </div>
  <div class="abs stay" style="left:462px;background:linear-gradient(180deg,rgba(0,0,0,0) 60%,rgba(0,0,0,.35)),linear-gradient(170deg,#cdd3da,#8d918a 40%,#5e7a3e)" role="img" aria-label="Chalet garden with mountains behind">
    <span class="label">6 Night</span><span class="go"><svg width="12" height="12" viewBox="0 0 12 12"><path d="M2 10L10 2M4 2h6v6" fill="none" stroke="#5aaebc" stroke-width="1.6"/></svg></span>
  </div>
  <div class="abs stay" style="left:762px;background:linear-gradient(180deg,rgba(0,0,0,0) 60%,rgba(0,0,0,.35)),linear-gradient(160deg,#b9d2e6,#ddd8d0 45%,#6c7a8c)" role="img" aria-label="Guests sharing a meal at a table">
    <span class="label">4 Night</span><span class="go"><svg width="12" height="12" viewBox="0 0 12 12"><path d="M2 10L10 2M4 2h6v6" fill="none" stroke="#5aaebc" stroke-width="1.6"/></svg></span>
  </div>
  <div class="btn" style="left:520px;top:453px;width:161px;height:41px">View All Stays</div>
</section>

<section class="gallery" role="img" aria-label="Dusky mountain lake and chalet backdrop">
  <div class="abs head" style="top:56px">
    <div class="eyebrow">Gallery</div>
    <h2>Our Gallery</h2>
    <p>Welcome to our Gather Your Light chapters dedicated to empowering guests with valuable knowledge and resources.</p>
  </div>
  <div class="abs tile" style="left:161px;top:205px;width:429px;height:425px;background:linear-gradient(180deg,#d6e8f5,#a9c6dc 55%,#6f7f95 75%,#7b6d5c)" role="img" aria-label="Video: couple sitting together on a mountain rock">
    <svg class="play" width="34" height="40" viewBox="0 0 34 40"><path d="M0 0l34 20L0 40z" fill="#fff"/></svg>
  </div>
  <div class="abs tile" style="left:612px;top:205px;width:427px;height:199px;background:linear-gradient(170deg,#9ab6d4,#cfcac2 55%,#4e5d7a)" role="img" aria-label="Group of guests at a lakeside lunch"></div>
  <div class="abs tile" style="left:612px;top:428px;width:202px;height:202px;background:linear-gradient(170deg,#b8bfc6,#7f8378 45%,#5d8a36)" role="img" aria-label="Chalet lawn beneath the peaks"></div>
  <div class="abs tile" style="left:836px;top:428px;width:203px;height:202px;background:linear-gradient(165deg,#6a93c0,#395670 55%,#5a4a30)" role="img" aria-label="Wooden terrace overlooking the valley"></div>
  <div class="btn" style="left:520px;top:676px;width:161px;height:40px">View All Gallery</div>
</section>

<section class="testi">
  <div class="abs head" style="top:56px">
    <div class="eyebrow">Our Testimonial</div>
    <h2>Our Testimonial</h2>
    <p>Welcome to our Gather Your Light chapters dedicated to empowering guests with valuable knowledge and resources.</p>
  </div>
  <div class="abs card" style="left:199px">
    <div class="avatar" role="img" aria-label="Guest portrait"></div>
    <div class="who">Léa Martin<br><b>Alpine Hollow Co.</b></div>
    <div class="quote">“</div>
    <p>It was pleasure to work with Northfield. it's helped<br>us in our contributed his technical expertise.</p>
  </div>
  <div class="abs card" style="left:617px">
    <div class="avatar" role="img" aria-label="Guest portrait"></div>
    <div class="who">Léa Martin<br><b>Alpine Hollow Co.</b></div>
    <div class="quote">“</div>
    <p>It was pleasure to work with Northfield. it's helped<br>us in our contributed his technical expertise.</p>
  </div>
  <div class="btn" style="left:512px;top:446px;width:176px;height:41px">View All Testimonial</div>
</section>

<section class="blog">
  <div class="abs head" style="top:56px">
    <div class="eyebrow">Our Latest Blog</div>
    <h2>Latest Posts &amp; Articles</h2>
    <p>Welcome to our Gather Your Light chapters dedicated to empowering guests with valuable knowledge and resources.</p>
  </div>
  <article class="abs post" style="left:161px">
    <div class="body">
      <div class="cat">MOUNTAIN NOTES</div>
      <div class="date">Mar 25, 2025</div>
      <h3>How to Choose the Best<br>In-Home Pet Care Service</h3>
      <p>Consectetuer fringilla aenean sagittis<br>potenti ullamcorper nam porta<br>feugiat. Ante urna congue feugiat<br>efficitur vel duis.</p>
      <span class="more">LEARN MORE &nbsp;›</span>
    </div>
    <div class="pic" style="background:linear-gradient(170deg,#9ab6d4,#d3cec6 50%,#5d6a80)" role="img" aria-label="Guests at a lunch table by the lake"></div>
  </article>
  <article class="abs post" style="left:620px">
    <div class="body">
      <div class="cat">MOUNTAIN NOTES</div>
      <div class="date">Mar 25, 2025</div>
      <h3>How to Choose the Best<br>In-Home Pet Care Service</h3>
      <p>Consectetuer fringilla aenean sagittis<br>potenti ullamcorper nam porta<br>feugiat. Ante urna congue feugiat<br>efficitur vel duis.</p>
      <span class="more">LEARN MORE &nbsp;›</span>
    </div>
    <div class="pic" style="background:linear-gradient(180deg,#3f78c4,#c9d8e8 40%,#5e9a3a 70%,#3f6e2a)" role="img" aria-label="Snowy peak above a green pasture and wooden chalet"></div>
  </article>
  <div class="btn" style="left:520px;top:572px;width:161px;height:41px;font-size:13px">VIEW ALL BLOG</div>
</section>

<footer class="foot">
  <div class="abs brand">GATHER<small>YOUR LIGHT</small></div>
  <p class="abs foot-about">It is a long established fact that a reader will be distracted by the readable content of a page when looking at its layout.</p>
  <div class="abs dot" style="left:161px;top:200px;background:var(--teal)"></div>
  <div class="abs dot" style="left:202px;top:200px;background:var(--teal)"></div>
  <div class="abs dot" style="left:243px;top:200px;background:var(--teal)"></div>

  <div class="abs" style="left:575px;top:57px">
    <h4>Quick Links</h4>
    <ul class="links"><li>Welcome</li><li>Our History</li><li>Our Stays</li><li>The Agenda</li><li>Contact</li></ul>
  </div>

  <div class="abs" style="left:831px;top:57px">
    <h4 style="margin-bottom:16px">Contact Us</h4>
    <div class="contact-row"><span class="ico"><svg width="12" height="12" viewBox="0 0 24 24"><path fill="#fff" d="M6.6 10.8a15 15 0 0 0 6.6 6.6l2.2-2.2c.3-.3.7-.4 1-.2 1.1.4 2.3.6 3.6.6.6 0 1 .4 1 1V20c0 .6-.4 1-1 1A17 17 0 0 1 3 4c0-.6.4-1 1-1h3.5c.6 0 1 .4 1 1 0 1.2.2 2.4.6 3.6.1.3 0 .7-.2 1z"/></svg></span>+41 22 555 01 47</div>
    <div class="contact-row"><span class="ico"><svg width="12" height="10" viewBox="0 0 24 18"><rect x="1" y="1" width="22" height="16" rx="2" fill="none" stroke="#fff" stroke-width="2.4"/><path d="M2 2l10 8 10-8" fill="none" stroke="#fff" stroke-width="2.4"/></svg></span>info@gatheryourlight.ch</div>
    <div class="contact-row"><span class="ico"><svg width="10" height="13" viewBox="0 0 20 26"><path fill="#fff" d="M10 0a10 10 0 0 0-10 10c0 7 10 16 10 16s10-9 10-16A10 10 0 0 0 10 0zm0 14a4 4 0 1 1 0-8 4 4 0 0 1 0 8z"/></svg></span>122 Rue des Pins</div>
  </div>

  <div class="abs rule"></div>
  <div class="abs copy">© 2025 Gather Your Light</div>
</footer>

</body>
</html>
```